University of Brellmoor - UB VyRta LOGO + Website Design

We need a LOGO and new website Design for a project called UB VyRta

The LOGO will be: We need a new Logo for a new innovative technology movement at the UB the logo should embody some of these concepts:

New Tech, Ideation, Innovation, Events, People, Projects, Collaboration, badges, connections, gamification
The broad mission of the UB is Teaching, Research and Service

THEME CONCEPTS:
----------------------
OVERALL: IDEA -->> ( lightblub...) -> PLAN ( blue print or Rocket Design) --> paper airplane ( teamwork - collaboration... - assembly) -->> LAUNCHED ROCKET ( A New service )

IDEAS: For the "lightbulb" stage... when someone is putting an idea together, it might be cool to show a campfire w/ people sitting around it, discussing... perhaps w/ stars/moon above (dreaming of what could be)

THE WEBSITE Components of the site will include:

1. Search.
2. An Idea Leader Board
3. Events, Team Meetups, Conferences, etc
4. A Project Leader Board with New Project Quests
5. Digital Badges
6. Workflow: Ideas -> Projects -> Collaborative Services -> Teamwork!
7. Gamification of Work

All areas should feature and highlight what is NEW and TRENDING up in popularity

Actions on the site will include:

1) Creating Ideas and Projects
2) Inviting people to Join the effort and Collaborate with funding or resources
3) People Profiles
4) Ideas move through a workflow to Services
5) RSVP for Events
6) Gamification techniques to make the work more fun

Want to focus on these website components:

Header or Mast Head
Content Middle Region
Footer

MUST BE MOBILE FRIENDLY and RESPONSIVE DESIGN
Updates

Reason: Hi there Designers, Does anyone want to do some designs for the website, not just the logo... the site is live - it just has NO design - see http://ubvyrta.org - Does anyone have ideas for website designs for this project? With only 8 designs, My goal is to get about at least 10 website designs..... I will continue to delay this project, until I see some website designs... Have an idea for the website? Please submit your designs! Thanks, The UB Vyrta team

Reason: We need to see more options for the website designs.

Target Market(s)

The 7000 Information Technology workers across the University of Brellmoor

Industry/Entity Type

University

Logo Text

UB VyRta

Number of Pages Required

5+ page

Font styles to use
Sans Serif

Colors
3176b5
0792cd
fbf289
fbed22
e34197
9bcb3c
a64599
00a990
ec1f27

Requirements
Must have
• 1. Search.
• 2. An Idea Leader Board
• 3. Events, Team Meetups, Conferences, etc
• 4. A Project Leader Board with New Project Quests
• 5. Digital Badges
• 6. Workflow: Ideas -> Projects -> Collaborative Services -> Teamwork!
• 7. Gamification of Work
• THE WEBSITE Components of the site will include:
• 1. Search.
• 2. An Idea Leader Board
• 5. Digital Badges
• 7. Gamification of Work
• All areas should feature and highlight what is NEW and TRENDING up in popularity
• Actions on the site will include:
• 1) Creating Ideas and Projects
• 2) Inviting people to Join the effort and Collaborate with funding or resources
• 3) People Profiles
• 4) Ideas move through a workflow to Services
• 5) RSVP for Events
• 6) Gamification techniques to make the work more fun
• Want to focus on these website components:
• Header or Mast Head
• Content Middle Region
• Footer
Nice to have
• Digital Badges for successful Ideas, collaborations, team work, projects and leadership activities
Should not have
• DO NOT use the University of Brellmoor LOGO that looks like a flushing toilet - that logo was dropped and is banned from use....

```html
<!DOCTYPE html>
<html lang="en">
<head>
<meta charset="utf-8">
<title>UB VyRta — Mobile Navigation Layout</title>
<link rel="stylesheet" href="https://fonts.googleapis.com/css2?family=Open+Sans:wght@300;600;700;800&display=swap">
<style>
  :root {
    --page-bg: #e5e7e8;
    --navy: #1f5282;
    --navy-deep: #1d4f80;
    --brand-blue: #3176b5;
    --line: #2d6aa3;
    --lime: #9bcb3c;
    --magenta: #dc1b5a;
    --placeholder: #d4d5d6;
    --white: #ffffff;
    --card-border: #c8c9ca;
  }
  * { box-sizing: border-box; margin: 0; padding: 0; }
  html, body { width: 1027px; height: 1200px; overflow: hidden; }
  body {
    background: var(--page-bg);
    font-family: "Open Sans", Arial, sans-serif;
    position: relative;
  }
  .board-rule {
    position: absolute; left: 48px; top: 0;
    width: 499px; height: 7px; background: var(--navy);
  }
  .board-title {
    position: absolute; left: 48px; top: 35px;
    font-size: 10.5px; font-weight: 700; letter-spacing: 1.1px;
    color: var(--navy);
  }
  .board-brand {
    position: absolute; right: 30px; top: 10px;
    font-size: 44px; font-weight: 300; letter-spacing: 1px;
    color: var(--navy);
  }
  .screen { position: absolute; display: block; }
  .screen--phone-closed { left: 210px; top: 197px; width: 231px; height: 408px; }
  .screen--phone-open   { left: 549px; top: 197px; width: 230px; height: 408px; }
  .screen--tablet       { left: 164px; top: 724px; width: 613px; height: 407px; }

  .brand-text { font-family: "Open Sans", Arial, sans-serif; font-weight: 300; fill: var(--white); }
  .button-text { font-family: "Open Sans", Arial, sans-serif; font-weight: 700; font-size: 9.5px; fill: var(--white); }
  .menu-text { font-family: "Open Sans", Arial, sans-serif; font-weight: 700; font-size: 10.5px; letter-spacing: 1.2px; fill: var(--white); }
  .page-title { font-family: "Open Sans", Arial, sans-serif; font-weight: 700; font-size: 13.5px; fill: var(--brand-blue); }
</style>
</head>
<body>
  <div class="board-rule"></div>
  <p class="board-title">MOBILE NAVIGATION LAYOUT</p>
  <p class="board-brand">UB VyRta</p>

  <!-- Phone: navigation closed -->
  <svg class="screen screen--phone-closed" viewBox="0 0 225 397" aria-label="Phone landing page with closed navigation">
    <defs>
      <pattern id="p1-lines" width="175" height="13.6" patternUnits="userSpaceOnUse" y="271">
        <rect width="175" height="6" fill="#d4d5d6"/>
      </pattern>
    </defs>
    <rect width="225" height="397" fill="#3176b5"/>
    <!-- header -->
    <rect width="225" height="44" fill="#3176b5"/>
    <path d="M0 0 H20 L35 22 L20 44 H0 Z" fill="#1f5282"/>
    <g fill="none" stroke="#fff" stroke-width="1.6">
      <rect x="-8" y="13" width="18" height="4.5" rx="2.2"/>
      <rect x="-8" y="20" width="18" height="4.5" rx="2.2"/>
      <rect x="-8" y="27" width="18" height="4.5" rx="2.2"/>
    </g>
    <text class="brand-text" x="50" y="29" font-size="20">UB VyRta</text>
    <rect x="186" y="0" width="39" height="44" fill="#1f5282"/>
    <circle cx="206" cy="19" r="8" fill="none" stroke="#fff" stroke-width="1.6"/>
    <line x1="200" y1="25" x2="195" y2="31" stroke="#fff" stroke-width="1.6"/>
    <!-- search -->
    <rect y="44" width="225" height="38" fill="#1f5282"/>
    <rect x="6" y="48" width="157" height="30" fill="#3176b5"/>
    <rect x="162" y="48" width="60" height="30" fill="#9bcb3c"/>
    <text class="button-text" x="192" y="66" text-anchor="middle">SEARCH</text>
    <!-- page -->
    <rect y="82" width="225" height="60" fill="#fff"/>
    <text class="page-title" x="11" y="102">Landing page</text>
    <rect x="11" y="116.5" width="203" height="290" fill="#fff" stroke="#c8c9ca"/>
    <rect x="23" y="131" width="175" height="19" fill="#d4d5d6"/>
    <rect x="23" y="161" width="175" height="19" fill="#d4d5d6"/>
    <rect x="23" y="191" width="173" height="67" fill="#dc1b5a"/>
    <rect x="23" y="271" width="175" height="126" fill="url(#p1-lines)"/>
  </svg>

  <!-- Phone: navigation open -->
  <svg class="screen screen--phone-open" viewBox="0 0 224 397" aria-label="Phone with open navigation drawer">
    <defs>
      <pattern id="p2-lines" width="100" height="13.6" patternUnits="userSpaceOnUse" y="271">
        <rect width="100" height="6" fill="#d4d5d6"/>
      </pattern>
    </defs>
    <rect width="224" height="397" fill="#3176b5"/>
    <!-- page peeking out -->
    <rect x="145" y="44" width="79" height="36" fill="#1f5282"/>
    <rect x="150" y="48" width="74" height="30" fill="#3176b5"/>
    <rect x="145" y="80" width="79" height="60" fill="#fff"/>
    <text class="page-title" x="155" y="101">Landing page</text>
    <rect x="157.5" y="116.5" width="80" height="290" fill="#fff" stroke="#c8c9ca"/>
    <rect x="169" y="131" width="60" height="19" fill="#d4d5d6"/>
    <rect x="169" y="161" width="60" height="19" fill="#d4d5d6"/>
    <rect x="169" y="191" width="60" height="67" fill="#dc1b5a"/>
    <rect x="169" y="271" width="60" height="126" fill="url(#p2-lines)"/>
    <!-- header -->
    <rect width="224" height="44" fill="#3176b5"/>
    <path d="M0 0 H163 L177 22 L163 44 H0 Z" fill="#1f5282"/>
    <rect x="24" y="7" width="74" height="32" rx="2" fill="#9bcb3c"/>
    <text class="button-text" x="61" y="26.5" text-anchor="middle">LOG IN</text>
    <g fill="none" stroke="#fff" stroke-width="1.6">
      <rect x="132" y="13" width="24" height="4.5" rx="2.2"/>
      <rect x="132" y="20" width="24" height="4.5" rx="2.2"/>
      <rect x="132" y="27" width="24" height="4.5" rx="2.2"/>
    </g>
    <text class="brand-text" x="192" y="29" font-size="20">UB VyRta</text>
    <!-- drawer -->
    <rect x="0" y="44" width="145" height="353" fill="#1f5282"/>
    <rect x="0" y="200" width="145" height="52" fill="#3176b5"/>
    <g stroke="#2d6aa3" stroke-width="1">
      <line x1="0" y1="96" x2="145" y2="96"/>
      <line x1="0" y1="148" x2="145" y2="148"/>
      <line x1="0" y1="200" x2="145" y2="200"/>
    </g>
    <g fill="none" stroke="#fff" stroke-width="1.4">
      <circle cx="33" cy="70" r="10"/>
      <circle cx="33" cy="122" r="10"/>
      <circle cx="33" cy="174" r="10"/>
      <circle cx="33" cy="278" r="10"/>
    </g>
    <circle cx="33" cy="226" r="10" fill="#fff"/>
    <text class="menu-text" x="59" y="74">PEOPLE</text>
    <text class="menu-text" x="59" y="126">IDEAS</text>
    <text class="menu-text" x="59" y="178">PROJECTS</text>
    <text class="menu-text" x="59" y="230">EVENTS</text>
    <text class="menu-text" x="59" y="282">ABOUT</text>
  </svg>

  <!-- Tablet -->
  <svg class="screen screen--tablet" viewBox="0 0 597 396" aria-label="Tablet landing page with sidebar navigation">
    <defs>
      <pattern id="t-lines-left" width="176" height="13.6" patternUnits="userSpaceOnUse" y="263">
        <rect width="176" height="6" fill="#d4d5d6"/>
      </pattern>
      <pattern id="t-lines-right" width="175" height="13.6" patternUnits="userSpaceOnUse" y="183">
        <rect width="175" height="6" fill="#d4d5d6"/>
      </pattern>
    </defs>
    <rect width="597" height="396" fill="#3176b5"/>
    <!-- header -->
    <path d="M0 0 H165 L180 22 L165 44 H0 Z" fill="#1f5282"/>
    <rect x="25" y="7" width="73" height="32" rx="2" fill="#9bcb3c"/>
    <text class="button-text" x="61.5" y="26.5" text-anchor="middle">LOG IN</text>
    <g fill="none" stroke="#fff" stroke-width="1.6">
      <rect x="131" y="13" width="25" height="4.5" rx="2.2"/>
      <rect x="131" y="20" width="25" height="4.5" rx="2.2"/>
      <rect x="131" y="27" width="25" height="4.5" rx="2.2"/>
    </g>
    <text class="brand-text" x="198" y="29" font-size="20">UB VyRta</text>
    <rect x="495" y="0" width="52" height="44" fill="#1f5282"/>
    <circle cx="522" cy="19" r="8" fill="none" stroke="#fff" stroke-width="1.6"/>
    <line x1="516" y1="25" x2="511" y2="31" stroke="#fff" stroke-width="1.6"/>
    <!-- search -->
    <rect x="145" y="44" width="452" height="36" fill="#1f5282"/>
    <rect x="152" y="48" width="381" height="28" fill="#3176b5"/>
    <rect x="532" y="48" width="60" height="28" fill="#9bcb3c"/>
    <text class="button-text" x="562" y="65" text-anchor="middle">SEARCH</text>
    <!-- page -->
    <rect x="145" y="80" width="452" height="60" fill="#fff"/>
    <text class="page-title" x="166" y="101">Landing page</text>
    <rect x="165.5" y="116.5" width="411" height="290" fill="#fff" stroke="#c8c9ca"/>
    <rect x="184" y="123" width="372" height="19" fill="#d4d5d6"/>
    <rect x="184" y="153" width="372" height="19" fill="#d4d5d6"/>
    <rect x="184" y="183" width="173" height="67" fill="#dc1b5a"/>
    <rect x="184" y="263" width="176" height="133" fill="url(#t-lines-left)"/>
    <rect x="381" y="183" width="175" height="213" fill="url(#t-lines-right)"/>
    <!-- sidebar -->
    <rect x="0" y="44" width="145" height="352" fill="#1f5282"/>
    <rect x="0" y="200" width="145" height="52" fill="#3176b5"/>
    <g stroke="#2d6aa3" stroke-width="1">
      <line x1="0" y1="96" x2="145" y2="96"/>
      <line x1="0" y1="148" x2="145" y2="148"/>
      <line x1="0" y1="200" x2="145" y2="200"/>
    </g>
    <g fill="none" stroke="#fff" stroke-width="1.4">
      <circle cx="35" cy="69" r="10"/>
      <circle cx="35" cy="121" r="10"/>
      <circle cx="35" cy="173" r="10"/>
      <circle cx="35" cy="225" r="10"/>
      <circle cx="35" cy="277" r="10"/>
    </g>
    <text class="menu-text" x="60" y="73">PEOPLE</text>
    <text class="menu-text" x="60" y="125">IDEAS</text>
    <text class="menu-text" x="60" y="177">PROJECTS</text>
    <text class="menu-text" x="60" y="229">EVENTS</text>
    <text class="menu-text" x="60" y="281">ABOUT</text>
  </svg>
</body>
</html>
```